KRV Business Cards

We are a local commercial development company based in Silicon Valley and we would like a new business card. I've attached a copy of our company brochure to give a flavor of what we do, our logo, info company colors/graphics, and our current business card. We don't necessarily need a crazy makeover, but would like something that feels a little bit more "fresh" and modern (we've had the same business card design for 15+ years), but still in keeping with our overall brand -- clean, high-quality, modern but timeless. Would like to add our website to the info on the card (www.velmara.com) and would like the flexibility for some folks to have an efax number listed and some not to have that included (without it looking like there is a hole).

```html
<!DOCTYPE html>
<html lang="en">
<head>
<meta charset="utf-8">
<title>KRV Business Card</title>
<link rel="stylesheet" href="https://fonts.googleapis.com/css2?family=Cinzel:wght@400&family=Mulish:wght@300;400&family=Arimo:wght@400&display=swap">
<style>
  :root {
    --brand-blue: #3e5b79;
    --brand-blue-light: #5a7fa3;
    --frame-line: #6f93b8;
    --icon-blue: #4f74a0;
    --ink-name: #34506e;
    --ink-gray: #6e6e6e;
    --paper: #fdfdfd;
    --page: #ffffff;
  }
  * { margin: 0; padding: 0; box-sizing: border-box; }
  html, body { width: 993px; height: 1200px; overflow: hidden; background: var(--page); }
  .canvas { position: relative; width: 993px; height: 1200px; }

  /* Front */
  .card-front {
    position: absolute; left: 39px; top: 39px; width: 915px; height: 521px;
    background: #fcfcfc;
  }
  .front-panel {
    position: absolute; left: 32px; top: 32px; width: 849px; height: 424px;
    background: radial-gradient(ellipse at 42% 42%, var(--brand-blue-light) 0%, var(--brand-blue) 85%);
  }
  .front-frame {
    position: absolute; left: 33px; top: 33px; width: 784px; height: 359px;
    border: 1.5px solid var(--frame-line);
  }
  .company-name {
    position: absolute; left: 158px; top: 96px;
    font-family: "Cinzel", serif; font-weight: 400; color: #fff;
    font-size: 74px; line-height: 80px; letter-spacing: 1px;
  }
  .company-name .suffix { font-size: 60px; }
  .website {
    position: absolute; left: 285px; top: 470px;
    display: flex; align-items: center; gap: 13px;
    font-family: "Mulish", sans-serif; font-weight: 300; font-size: 29px; color: var(--ink-gray);
  }

  /* Back */
  .card-back {
    position: absolute; left: 39px; top: 638px; width: 915px; height: 523px;
    background: radial-gradient(ellipse at 50% 40%, #587c9f 0%, var(--brand-blue) 90%);
  }
  .back-panel {
    position: absolute; left: 32px; top: 33px; width: 849px; height: 456px;
    background: var(--paper);
  }
  .person { position: absolute; left: 40px; top: 180px; }
  .person-name {
    font-family: "Arimo", sans-serif; font-size: 40px; color: var(--ink-name); letter-spacing: 0.3px; line-height: 44px;
  }
  .person-title {
    font-family: "Mulish", sans-serif; font-weight: 300; font-size: 29px; color: var(--ink-gray); margin-top: 2px;
  }
  .divider {
    position: absolute; left: 424px; top: 66px; height: 330px;
    border-left: 3px dotted var(--icon-blue);
  }
  .contact-list {
    position: absolute; left: 456px; top: 96px; list-style: none;
    font-family: "Mulish", sans-serif; font-weight: 300; font-size: 29px; color: var(--ink-gray);
    line-height: 40px;
  }
  .contact-list li { display: flex; align-items: center; gap: 18px; margin-bottom: 9px; }
  .contact-list svg { flex: none; width: 33px; height: 33px; }
  .icon { fill: none; stroke: var(--icon-blue); stroke-width: 1.6; }
  .icon-fill { fill: var(--icon-blue); stroke: none; }
</style>
</head>
<body>
<main class="canvas">
  <section class="card-front">
    <div class="front-panel">
      <div class="front-frame">
        <h1 class="company-name">KERROW<br>RIDGE<br>VENTURES, <span class="suffix">LLC</span></h1>
      </div>
    </div>
    <p class="website">
      <svg width="33" height="33" viewBox="0 0 34 34" aria-hidden="true">
        <circle class="icon" cx="17" cy="17" r="15.5"/>
        <circle class="icon" cx="17" cy="17" r="10"/>
        <ellipse class="icon" cx="17" cy="17" rx="4.5" ry="10"/>
        <line class="icon" x1="7" y1="17" x2="27" y2="17"/>
        <line class="icon" x1="9" y1="12" x2="25" y2="12"/>
        <line class="icon" x1="9" y1="22" x2="25" y2="22"/>
      </svg>
      www.velmara.com
    </p>
  </section>

  <section class="card-back">
    <div class="back-panel">
      <div class="person">
        <h2 class="person-name">HELENA J. MARSH</h2>
        <p class="person-title">Partner</p>
      </div>
      <div class="divider"></div>
      <ul class="contact-list">
        <li>
          <svg viewBox="0 0 34 34" aria-hidden="true">
            <circle class="icon" cx="17" cy="17" r="15.5"/>
            <path class="icon-fill" d="M17 7a7 7 0 0 0-7 7c0 5 7 13 7 13s7-8 7-13a7 7 0 0 0-7-7zm0 10a3 3 0 1 1 0-6 3 3 0 0 1 0 6z"/>
          </svg>
          <span>382 Harlow Street,<br>Menlo Park, CA 94025</span>
        </li>
        <li>
          <svg viewBox="0 0 34 34" aria-hidden="true">
            <circle class="icon" cx="17" cy="17" r="15.5"/>
            <path class="icon-fill" d="M11 8l3.5 0 1.5 5-2.2 1.6c1 2.4 2.6 4 4.9 5l1.6-2.2 5 1.5v3.5c0 1-1 1.8-2 1.6C15.5 23.5 10.5 18.5 9.4 10c-.2-1 .6-2 1.6-2z"/>
          </svg>
          <span>(main) 650.555.0142</span>
        </li>
        <li>
          <svg viewBox="0 0 34 34" aria-hidden="true">
            <circle class="icon" cx="17" cy="17" r="15.5"/>
            <rect class="icon" x="12" y="8" width="10" height="18" rx="1.5"/>
            <line class="icon" x1="15.5" y1="23" x2="18.5" y2="23"/>
          </svg>
          <span>(direct) 650.555.0163</span>
        </li>
        <li>
          <svg viewBox="0 0 34 34" aria-hidden="true">
            <circle class="icon" cx="17" cy="17" r="15.5"/>
            <rect class="icon-fill" x="8.5" y="11" width="17" height="12" rx="1"/>
            <path d="M9 12l8 6 8-6M9 22l6-5M25 22l-6-5" fill="none" stroke="#fff" stroke-width="1.3"/>
          </svg>
          <span>helena@velmara.com</span>
        </li>
        <li>
          <svg viewBox="0 0 34 34" aria-hidden="true">
            <circle class="icon" cx="17" cy="17" r="15.5"/>
            <rect class="icon" x="12" y="8.5" width="10" height="5"/>
            <rect class="icon" x="9" y="13.5" width="16" height="8" rx="1"/>
            <rect class="icon" x="12" y="19" width="10" height="6"/>
          </svg>
          <span>650.555.0199</span>
        </li>
      </ul>
    </div>
  </section>
</main>
</body>
</html>
```